Small Production Wine Needs a Wine Label Design

We need a wine bottle label design for a hand crafted Petite Sirah wine produced by two friends in the wine industry. The wine brand will be called, TK (the first initials of each of their last names, Tavares Kimble). The petite sirah grapes are from the Tavares vineyard in the Russian River Valley of Sonoma County, and Kimble is the winemaker. Tavares is a third generation farmer in sonoma county and also raised cattle on the same ranch the grapes were grown. Kimble is an experienced Winemaker and helped increase the quality of wines from Lodi, CA at a small boutique winery. For the front label, we would like the TK to look like a cattle brand, the font to be color black. We would like to include somewhere on the label Tavares Kimble, maybe underneath the cattle brand in smaller font. We also need to include the appellation on the label, Russian River Valley, and in smaller font Sonoma County. Also, the varietal of the wine is Petite Sirah and the vintage is 2013. We are aiming for a simple and relatively classy label, yet with a rustic touch. We would like the label to be rectangular and have an organic/linen look to it. Also the incorporation of a ridge or mountain range in the back ground or subtly in the label would be cool.

```html
<!DOCTYPE html>
<html lang="en">
<head>
<meta charset="utf-8">
<title>Tavares Kimble Petite Sirah Label</title>
<link rel="stylesheet" href="https://fonts.googleapis.com/css2?family=Dancing+Script:wght@600&family=Josefin+Sans:wght@300;400&display=swap">
<style>
  :root {
    --backdrop: #e9e3d3;
    --paper-light: #e4d9bd;
    --paper-mid: #d8caa6;
    --paper-edge: #c9b78f;
    --ink-dark: #3b2618;
    --ink-brown: #5a3a22;
    --ridge-brown: #8a5a34;
  }
  * { margin: 0; padding: 0; box-sizing: border-box; }
  html, body {
    width: 1200px;
    height: 1000px;
    overflow: hidden;
    background: var(--backdrop);
  }
  .canvas {
    position: relative;
    width: 1200px;
    height: 1000px;
  }
  .label {
    position: absolute;
    left: 311px;
    top: 98px;
    width: 578px;
    height: 806px;
    background:
      radial-gradient(ellipse at 50% 45%, var(--paper-light) 0%, var(--paper-mid) 70%, var(--paper-edge) 100%);
    box-shadow: 0 2px 6px rgba(60, 40, 20, 0.15);
    text-align: center;
    color: var(--ink-brown);
  }
  .ridge-art {
    position: absolute;
    left: 95px;
    top: 78px;
    width: 436px;
    height: 96px;
  }
  .brand-mark {
    position: absolute;
    left: 0;
    right: 0;
    top: 200px;
    font-family: "Dancing Script", cursive;
    font-weight: 600;
    font-size: 168px;
    line-height: 170px;
    color: var(--ink-dark);
  }
  .brand-name {
    position: absolute;
    left: 0;
    right: 0;
    top: 388px;
    font-family: "Dancing Script", cursive;
    font-weight: 600;
    font-size: 54px;
    line-height: 64px;
    color: var(--ink-dark);
    letter-spacing: 1px;
  }
  .varietal {
    position: absolute;
    left: 0;
    right: 0;
    top: 514px;
    display: flex;
    align-items: center;
    justify-content: center;
    gap: 18px;
    font-family: "Josefin Sans", sans-serif;
    font-weight: 300;
    font-size: 33px;
    line-height: 44px;
    color: var(--ink-brown);
  }
  .varietal .rule {
    display: block;
    width: 52px;
    height: 2px;
    background: var(--ink-brown);
  }
  .appellation {
    position: absolute;
    left: 0;
    right: 0;
    top: 612px;
    font-family: "Dancing Script", cursive;
    font-weight: 600;
    font-size: 38px;
    line-height: 50px;
    color: var(--ink-brown);
  }
  .county {
    position: absolute;
    left: 0;
    right: 0;
    top: 662px;
    font-family: "Dancing Script", cursive;
    font-weight: 600;
    font-size: 36px;
    line-height: 50px;
    color: var(--ink-brown);
  }
  .vintage {
    position: absolute;
    left: 0;
    right: 0;
    top: 730px;
    font-family: "Josefin Sans", sans-serif;
    font-weight: 300;
    font-size: 36px;
    line-height: 44px;
    color: var(--ink-brown);
  }
</style>
</head>
<body>
  <main class="canvas">
    <section class="label">
      <svg class="ridge-art" viewBox="0 0 436 96" role="img" aria-label="Hand-drawn mountain ridge illustration in brown ink">
        <defs>
          <linearGradient id="ridgeFill" x1="0" y1="0" x2="0" y2="1">
            <stop offset="0" stop-color="#8a5a34" stop-opacity="0.55"/>
            <stop offset="1" stop-color="#8a5a34" stop-opacity="0.15"/>
          </linearGradient>
        </defs>
        <rect x="0" y="0" width="436" height="96" fill="url(#ridgeFill)"/>
      </svg>

      <div class="brand-mark">TK</div>
      <h1 class="brand-name">Tavares Kimble</h1>

      <p class="varietal"><span class="rule"></span>Petite Sirah<span class="rule"></span></p>

      <p class="appellation">Russian River Valley</p>
      <p class="county">Sonoma County</p>
      <p class="vintage">2013</p>
    </section>
  </main>
</body>
</html>
```